Lumen Keyvault Password Manager WebApp Design

Lumen Keyvault is seeking an expert UI designer to provide a fresh and modern visual appeal for our product. Our inspiration comes from two major tools that have successfully managed to balance functionality and design aesthetics - Orbix Folder and Vaultmint. We want our application to exude a similar trustworthiness and modernity, through a clean, intuitive and responsive design.
We have established preliminary mockups and would like the designer to work within these parameters while enhancing the overall user experience. The primary tasks will involve innovative and improved designs of the login screen and the password screen, both being crucial touchpoints for our users. The login screen also serves a crucial role in demonstrating how our system works.
Key Elements:
Logo Integration: We are providing the logo for Lumen Keyvault. The design should align with the logo, both in terms of colors and overall aesthetic, to ensure a cohesive brand identity.
Color Palette: The UI design should adhere to the color palette derived from the logo to maintain brand consistency. The design should effectively utilize these colors to highlight important elements and improve user engagement.
Trustworthy and Modern Design: The UI should be professional and trustworthy. It should mirror the look and feel of Orbix Folder's simplicity and Vaultmint's solid security design, which inspires user confidence.
Adherence to Mockup Boundaries: The existing mockups serve as a guideline for the layout and placement of elements. The design should respect these boundaries while bringing innovation and visual appeal.
Improved Login Screen: The login screen is a key part of the user's journey and should be designed with utmost care. It should be intuitive, easy-to-use, visually engaging, and educative, showcasing how the system operates and encouraging users to sign in with confidence.
Enhanced Password Screen: The password screen, another key user touchpoint, needs improvement. The different types of passwords should be made more visible and intuitive, easing user interaction and enhancing the overall experience.
Prospective designers are encouraged to test our current version available for free at app.lumenkeyvault.com to understand the product better and contribute to meaningful design enhancements.
The goal of this project is to provide a visually compelling and user-friendly interface for Lumen Keyvault that inspires user trust, while adhering to the branding elements, including color scheme and logo design. The ideal designer will have a proven track record of creating compelling UI designs that enhance user experience and engagement.
We preferred the design to be in Figma.
Please provide the 3 design so we can evaluate if we like to choice you:
1. Login Page.
2. Passwords View design
3. Single Passwod Page
We need all the pages to be design that are provided as screenshots.

```html
<!DOCTYPE html>
<html lang="en">
<head>
<meta charset="utf-8">
<title>Lumen Keyvault – App Screens</title>
<link href="https://fonts.googleapis.com/css2?family=Inter:wght@400;500;600;700&display=swap" rel="stylesheet">
<style>
:root{
  --bg:#0b3a7e;
  --blue:#0a63e8;
  --blue-soft:#4a8ef2;
  --surface:#eff3f8;
  --card:#ffffff;
  --ink:#1b1f4a;
  --muted:#62688a;
  --link:#0b55c9;
  --chip:#e4e9f2;
  --danger:#ef1c1c;
  --danger-soft:#fde3e4;
  --warn-band:#f2dde2;
}
*{box-sizing:border-box;margin:0;padding:0}
html,body{width:1200px;height:1200px;overflow:hidden}
body{background:var(--bg);font-family:'Inter',sans-serif;color:var(--ink);position:relative}
.screen{position:absolute;width:252px;height:546px;border-radius:20px;background:var(--surface);overflow:hidden}
.screen.blue{background:var(--blue)}
.abs{position:absolute}
.title{position:absolute;left:0;right:0;top:19px;text-align:center;font-size:15px;font-weight:700}
.blue .title{color:#fff}
.icon-btn{position:absolute;width:28px;height:28px;border-radius:8px;background:var(--chip);display:flex;align-items:center;justify-content:center}
.blue .icon-btn{background:rgba(255,255,255,.14)}
.card{position:absolute;background:var(--card);border-radius:16px;box-shadow:0 3px 8px rgba(20,40,90,.06)}
.name{font-size:9.5px;font-weight:600;color:var(--ink)}
.sub{font-size:8px;font-weight:500;color:var(--muted);margin-top:3px;line-height:1.25}
.btn{position:absolute;border-radius:8px;background:var(--blue);color:#fff;font-size:9.5px;font-weight:600;display:flex;align-items:center;justify-content:center;gap:5px}
.btn.outline{background:#fff;color:var(--link);border:1px solid var(--blue)}
.trash{position:absolute;width:28px;height:27px;border-radius:8px;background:var(--danger-soft);display:flex;align-items:center;justify-content:center}
.nav{position:absolute;background:var(--card);border-radius:12px;display:flex;justify-content:space-around;align-items:center}
.nav-item{display:flex;flex-direction:column;align-items:center;gap:7px;font-size:8px;font-weight:500;color:#858aa3}
.nav-item .ico{width:28px;height:28px;border-radius:9px;background:var(--chip);display:flex;align-items:center;justify-content:center}
.nav-item.active{color:var(--link);font-weight:600}
.nav-item.active .ico{background:#dbe6fb}
.menu-item{position:absolute;left:20px;display:flex;align-items:center;gap:7px;font-size:9.5px;font-weight:600;color:var(--link)}
.brand-dot{position:absolute;border-radius:50%;background:#050505}
.team-art{position:absolute;border-radius:8px;background:linear-gradient(135deg,#f6b26b,#3c8ee8)}
.stat{position:absolute;background:var(--card);border-radius:14px;text-align:center;display:flex;flex-direction:column;justify-content:center}
.stat b{font-size:9.5px;font-weight:600}
.stat span{font-size:8px;color:var(--muted);font-weight:500;margin-top:3px}
.cat{position:absolute;left:9px;width:122px;height:28px;border-radius:8px;display:flex;align-items:center;gap:7px;padding-left:17px;color:#fff;font-size:9.5px;font-weight:600}
.cat.active{background:var(--blue-soft)}
.price{position:absolute;right:10px;font-size:15px;font-weight:700}
.desc{position:absolute;left:9px;right:14px;font-size:7.8px;font-weight:500;color:var(--muted);line-height:1.27}
</style>
</head>
<body>

<svg width="0" height="0" style="position:absolute">
  <defs>
    <g id="i-stack"><rect x="1" y="1.5" width="8" height="6" rx="1" fill="none" stroke="currentColor" stroke-width="1"/><path d="M3 9.5h7.5V4" fill="none" stroke="currentColor" stroke-width="1"/></g>
    <g id="i-home"><path d="M1 5L5 1.5 9 5v4H6.2V6.5H3.8V9H1z" fill="#1b1f4a"/></g>
    <g id="i-group"><circle cx="3" cy="3.5" r="1.3" fill="#1b1f4a"/><circle cx="7" cy="3.5" r="1.3" fill="#1b1f4a"/><circle cx="5" cy="3" r="1.4" fill="#1b1f4a"/><path d="M1 7.5c0-1.5 8-1.5 8 0V8H1z" fill="#1b1f4a"/></g>
    <g id="i-bell"><path d="M5 1c2 0 2.8 1.5 2.8 3.3V6.5L9 8H1l1.2-1.5V4.3C2.2 2.5 3 1 5 1z" fill="currentColor"/><circle cx="5" cy="9" r="1" fill="currentColor"/></g>
    <g id="i-menu"><path d="M1 2h8M1 5h8M1 8h8" stroke="currentColor" stroke-width="1.1"/></g>
    <g id="i-trash"><path d="M2 3h6l-.6 6H2.6z M1.5 2h7 M4 1h2" stroke="#ef1c1c" stroke-width="1" fill="#ef1c1c"/></g>
    <g id="i-arrow"><path d="M1 5h8M6 2l3 3-3 3" fill="none" stroke="currentColor" stroke-width="1.3"/></g>
    <g id="i-info"><circle cx="5" cy="5" r="4" fill="none" stroke="#1b1f4a" stroke-width="1"/><path d="M5 4.3v3M5 2.8v.5" stroke="#1b1f4a" stroke-width="1"/></g>
    <g id="i-lock"><rect x="2" y="4.3" width="6" height="5" rx="1" fill="currentColor"/><path d="M3.2 4.3V3a1.8 1.8 0 013.6 0v1.3" fill="none" stroke="currentColor" stroke-width="1"/></g>
  </defs>
</svg>

<!-- Transfer -->
<section class="screen blue" style="left:187px;top:35px">
  <div class="icon-btn" style="left:14px;top:14px"><svg width="12" height="12" viewBox="0 0 10 10" style="color:#fff;transform:scaleX(-1)"><use href="#i-arrow"/></svg></div>
  <h1 class="title">Transfer</h1>
  <p class="abs" style="left:20px;right:20px;top:78px;text-align:center;color:#fff;font-size:9.5px;font-weight:600;line-height:1.2">You can import/export your accounts from other password managers.</p>
  <div class="card" style="left:9px;top:132px;width:233px;height:360px;border-radius:20px">
    <div class="abs" role="img" aria-label="Illustration of a globe circled by import and export arrows" style="left:15px;top:64px;width:202px;height:169px;border-radius:6px;background:radial-gradient(circle at 50% 50%,#cfd8e6 0,#e8eef7 45%,#f7f9fc 75%)"></div>
    <div class="btn" style="left:19px;top:297px;width:91px;height:29px"><svg width="12" height="12" viewBox="0 0 10 10"><circle cx="5" cy="5" r="4.6" fill="#fff"/><path d="M5 7.5V3M3 4.5L5 2.5 7 4.5" stroke="#0a63e8" stroke-width="1.1" fill="none"/></svg>Import</div>
    <div class="btn" style="left:117px;top:297px;width:91px;height:29px"><svg width="12" height="12" viewBox="0 0 10 10"><circle cx="5" cy="5" r="4.6" fill="#fff"/><path d="M5 2.5V7M3 5.5L5 7.5 7 5.5" stroke="#0a63e8" stroke-width="1.1" fill="none"/></svg>Export</div>
  </div>
</section>

<!-- Activities -->
<section class="screen" style="left:463px;top:35px">
  <h1 class="title">Activities</h1>
  <div class="card" style="left:9px;top:56px;width:233px;height:57px">
    <div class="abs" role="img" aria-label="Profile photo of the sharing user" style="left:9px;top:9px;width:38px;height:38px;border-radius:50%;background:linear-gradient(135deg,#c9a27a,#6b7a5a)"></div>
    <div class="abs" style="left:56px;top:11px;width:130px">
      <div class="name">Shared account Test 999</div>
      <div class="sub">Mara Olsen removed your access</div>
    </div>
    <div class="trash" style="left:196px;top:15px"><svg width="10" height="10" viewBox="0 0 10 10"><use href="#i-trash"/></svg></div>
  </div>
  <div class="card" style="left:9px;top:126px;width:233px;height:147px">
    <div class="abs" style="left:9px;top:9px;width:38px;height:38px;border-radius:50%;background:#fff;border:1px solid #e1e5ee"></div>
    <div class="abs" style="left:56px;top:10px;width:133px">
      <div class="name" style="line-height:1.18">The free trial has expired. Your account hase been automatically downgraded to Lite. To continue using all the benefits of the Pro plan, please consider upgrading.</div>
      <div class="sub" style="margin-top:7px">Lumen Keyvault</div>
    </div>
    <div class="trash" style="left:196px;top:9px"><svg width="10" height="10" viewBox="0 0 10 10"><use href="#i-trash"/></svg></div>
    <div class="btn" style="left:58px;top:110px;width:117px;height:29px">View details <svg width="10" height="10" viewBox="0 0 10 10" style="color:#fff"><use href="#i-arrow"/></svg></div>
  </div>
  <nav class="nav" style="left:9px;top:475px;width:222px;height:60px">
    <div class="nav-item"><span class="ico"><svg width="10" height="10" viewBox="0 0 10 10"><use href="#i-home"/></svg></span>Home</div>
    <div class="nav-item"><span class="ico"><svg width="10" height="10" viewBox="0 0 10 10"><use href="#i-group"/></svg></span>Group</div>
    <div class="nav-item active"><span class="ico"><svg width="10" height="10" viewBox="0 0 10 10" style="color:#0a63e8"><use href="#i-bell"/></svg></span>Activity</div>
    <div class="nav-item"><span class="ico"><svg width="10" height="10" viewBox="0 0 10 10" style="color:#1b1f4a"><use href="#i-menu"/></svg></span>More</div>
  </nav>
</section>

<!-- Overview -->
<section class="screen" style="left:738px;top:35px">
  <h1 class="title">Overview</h1>
  <div class="card" style="left:10px;top:55px;width:232px;height:57px">
    <div class="brand-dot" style="left:9px;top:9px;width:38px;height:38px"></div>
    <div class="abs" style="left:56px;top:16px"><div class="name">Harbor Team</div><div class="sub">harbor.team@lumenkeyvault.com</div></div>
  </div>
  <h2 class="abs" style="left:10px;top:131px;font-size:15px;font-weight:700">Current plan</h2>
  <div class="card" style="left:10px;top:166px;width:232px;height:57px">
    <div class="team-art" role="img" aria-label="Illustration of two team members" style="left:12px;top:13px;width:34px;height:30px"></div>
    <div class="abs" style="left:56px;top:16px"><div class="name">Small Team</div><div class="sub">Expired in: 10 / 01 / 2024</div></div>
  </div>
  <div class="stat" style="left:9px;top:233px;width:111px;height:57px"><b>66 / 100</b><span>Passwords</span></div>
  <div class="stat" style="left:130px;top:233px;width:111px;height:57px"><b>1</b><span>Shared Passwords</span></div>
  <div class="menu-item" style="top:318px"><svg width="11" height="11" viewBox="0 0 11 11"><use href="#i-stack"/></svg>Auth method</div>
  <div class="menu-item" style="top:355px"><svg width="11" height="11" viewBox="0 0 11 11"><use href="#i-stack"/></svg>Preferences</div>
  <div class="menu-item" style="top:393px"><svg width="11" height="11" viewBox="0 0 11 11"><use href="#i-stack"/></svg>Billing</div>
  <div class="menu-item" style="top:430px"><svg width="11" height="11" viewBox="0 0 11 11"><use href="#i-stack"/></svg>Password Generator</div>
  <div class="menu-item" style="top:467px"><svg width="11" height="11" viewBox="0 0 11 11"><use href="#i-stack"/></svg>Export / Import</div>
  <nav class="nav" style="left:9px;top:475px;width:222px;height:60px">
    <div class="nav-item"><span class="ico"><svg width="10" height="10" viewBox="0 0 10 10"><use href="#i-home"/></svg></span>Home</div>
    <div class="nav-item"><span class="ico"><svg width="10" height="10" viewBox="0 0 10 10"><use href="#i-group"/></svg></span>Group</div>
    <div class="nav-item"><span class="ico"><svg width="10" height="10" viewBox="0 0 10 10" style="color:#1b1f4a"><use href="#i-bell"/></svg></span>Activity</div>
    <div class="nav-item active"><span class="ico"><svg width="10" height="10" viewBox="0 0 10 10" style="color:#0a63e8"><use href="#i-menu"/></svg></span>More</div>
  </nav>
</section>

<!-- Categories -->
<section class="screen blue" style="left:187px;top:619px">
  <h1 class="title">Categories</h1>
  <div class="cat active" style="top:144px"><svg width="11" height="11" viewBox="0 0 11 11"><use href="#i-stack"/></svg>General</div>
  <div class="cat" style="top:177px"><svg width="11" height="11" viewBox="0 0 11 11"><use href="#i-stack"/></svg>Shared with me</div>
  <div class="cat" style="top:210px"><svg width="11" height="11" viewBox="0 0 11 11"><use href="#i-stack"/></svg>Work</div>
  <div class="cat" style="top:242px"><svg width="11" height="11" viewBox="0 0 11 11"><use href="#i-stack"/></svg>Social media</div>
  <div class="cat" style="top:275px"><svg width="11" height="11" viewBox="0 0 11 11"><use href="#i-stack"/></svg>Shopping</div>
  <div class="cat" style="top:308px"><svg width="11" height="11" viewBox="0 0 11 11"><use href="#i-stack"/></svg>Travel</div>
  <div class="cat" style="top:341px"><svg width="11" height="11" viewBox="0 0 11 11"><use href="#i-stack"/></svg>Banking</div>
  <div class="cat" style="top:374px"><svg width="11" height="11" viewBox="0 0 11 11"><use href="#i-stack"/></svg>Emails</div>

  <div class="abs" style="left:144px;top:65px;width:130px;height:449px;border-radius:14px;background:var(--surface);overflow:hidden">
    <div class="abs" style="left:77px;top:16px;font-size:12px;font-weight:700;white-space:nowrap">Overview</div>
    <div class="card" style="left:8px;top:45px;width:130px;height:47px;border-radius:12px">
      <div class="brand-dot" style="left:7px;top:8px;width:31px;height:31px"></div>
      <div class="abs" style="left:46px;top:13px;white-space:nowrap"><div class="name" style="font-size:8px">Harbor Team</div><div class="sub" style="font-size:6.5px;margin-top:2px">harbor.team@lumenkeyvault.com</div></div>
    </div>
    <div class="abs" style="left:8px;top:107px;font-size:12px;font-weight:700">Current plan</div>
    <div class="card" style="left:8px;top:138px;width:130px;height:46px;border-radius:12px">
      <div class="team-art" role="img" aria-label="Illustration of two team members" style="left:10px;top:11px;width:28px;height:24px"></div>
      <div class="abs" style="left:46px;top:13px;white-space:nowrap"><div class="name" style="font-size:8px">Small Team</div><div class="sub" style="font-size:6.5px;margin-top:2px">Expired in: 10 / 01 / 2024</div></div>
    </div>
    <div class="stat" style="left:8px;top:192px;width:91px;height:46px;border-radius:12px"><b style="font-size:8px">66 / 100</b><span style="font-size:6.5px">Passwords</span></div>
    <div class="menu-item" style="left:16px;top:261px;font-size:7.8px;gap:6px"><svg width="9" height="9" viewBox="0 0 11 11"><use href="#i-stack"/></svg>Auth method</div>
    <div class="menu-item" style="left:16px;top:292px;font-size:7.8px;gap:6px"><svg width="9" height="9" viewBox="0 0 11 11"><use href="#i-stack"/></svg>Preferences</div>
    <div class="menu-item" style="left:16px;top:323px;font-size:7.8px;gap:6px"><svg width="9" height="9" viewBox="0 0 11 11"><use href="#i-stack"/></svg>Billing</div>
    <div class="menu-item" style="left:16px;top:354px;font-size:7.8px;gap:6px;white-space:nowrap"><svg width="9" height="9" viewBox="0 0 11 11"><use href="#i-stack"/></svg>Password Generator</div>
    <div class="menu-item" style="left:16px;top:385px;font-size:7.8px;gap:6px;white-space:nowrap"><svg width="9" height="9" viewBox="0 0 11 11"><use href="#i-stack"/></svg>Export / Import</div>
    <nav class="nav" style="left:8px;top:391px;width:160px;height:50px;justify-content:flex-start;gap:22px;padding-left:11px">
      <div class="nav-item" style="font-size:6.5px;gap:5px"><span class="ico" style="width:23px;height:23px"><svg width="8" height="8" viewBox="0 0 10 10"><use href="#i-home"/></svg></span>Home</div>
      <div class="nav-item" style="font-size:6.5px;gap:5px"><span class="ico" style="width:23px;height:23px"><svg width="8" height="8" viewBox="0 0 10 10"><use href="#i-group"/></svg></span>Group</div>
    </nav>
  </div>
</section>

<!-- Email Account -->
<section class="screen" style="left:463px;top:619px">
  <div class="icon-btn" style="left:9px;top:15px"><svg width="11" height="11" viewBox="0 0 10 10"><path d="M2 2l6 6M8 2L2 8" stroke="#1b1f4a" stroke-width="1.2"/></svg></div>
  <h1 class="title">Email Account</h1>
  <div class="icon-btn" style="left:214px;top:15px"><svg width="11" height="11" viewBox="0 0 10 10"><path d="M1.5 1.5h5.5l1.5 1.5v5.5h-7z" fill="none" stroke="#1b1f4a" stroke-width="1"/><rect x="3" y="5.3" width="4" height="3.2" fill="none" stroke="#1b1f4a" stroke-width="1"/><path d="M3 1.5v2h3.5v-2" fill="none" stroke="#1b1f4a" stroke-width="1"/></svg></div>
  <div class="abs" style="left:9px;top:56px;width:233px;height:27px;border-radius:9px;background:var(--warn-band);color:var(--danger);font-size:9.5px;font-weight:600;display:flex;align-items:center;justify-content:center">Changes are not saved</div>
  <div class="card" style="left:9px;top:94px;width:233px;height:57px">
    <div class="brand-dot" style="left:9px;top:9px;width:38px;height:38px"></div>
    <div class="abs" style="left:56px;top:17px"><div class="name">Harbor Team</div><div class="sub">Me</div></div>
    <div class="icon-btn" style="left:196px;top:15px;background:#e2eafb"><svg width="11" height="11" viewBox="0 0 10 10"><path d="M1.5 8.5l.4-2L6.8 1.6l1.6 1.6L3.5 8.1z" fill="#0a63e8"/></svg></div>
  </div>
  <div class="abs" style="left:205px;top:427px;width:37px;height:37px;border-radius:9px;background:var(--blue);display:flex;align-items:center;justify-content:center"><svg width="14" height="14" viewBox="0 0 10 10"><circle cx="5" cy="5" r="4" fill="none" stroke="#fff" stroke-width=".9"/><path d="M5 3v4M3 5h4" stroke="#fff" stroke-width=".9"/></svg></div>
  <nav class="nav" style="left:9px;top:475px;width:233px;height:61px">
    <div class="nav-item"><span class="ico"><svg width="11" height="11" viewBox="0 0 10 10"><use href="#i-info"/></svg></span>Information</div>
    <div class="nav-item active"><span class="ico"><svg width="11" height="11" viewBox="0 0 10 10" style="color:#0a63e8"><use href="#i-lock"/></svg></span>Access</div>
  </nav>
</section>

<!-- Billing -->
<section class="screen" style="left:738px;top:619px">
  <div class="icon-btn" style="left:9px;top:15px"><svg width="11" height="11" viewBox="0 0 10 10" style="color:#1b1f4a;transform:scaleX(-1)"><use href="#i-arrow"/></svg></div>
  <h1 class="title">Billing</h1>
  <h2 class="abs" style="left:0;right:0;top:56px;text-align:center;font-size:15px;font-weight:700">Your current plan</h2>
  <div class="card" style="left:10px;top:92px;width:232px;height:144px">
    <div class="team-art" role="img" aria-label="Illustration of two team members" style="left:12px;top:13px;width:34px;height:30px"></div>
    <div class="abs" style="left:56px;top:17px"><div class="name">Small Team</div><div class="sub">per year</div></div>
    <div class="price" style="top:20px">$300</div>
    <p class="desc" style="top:58px">For small teams up to 10 members. This plan gives you ultimate tool to manage your team's passwords and collaborate internally. Available on all your devices.</p>
    <div class="btn outline" style="left:60px;top:105px;width:113px;height:29px">Learn more <svg width="10" height="10" viewBox="0 0 10 10" style="color:#0b55c9"><use href="#i-arrow"/></svg></div>
  </div>
  <h2 class="abs" style="left:67px;top:255px;font-size:15px;font-weight:700">Available plans</h2>
  <div class="card" style="left:10px;top:286px;width:232px;height:144px">
    <div class="team-art" role="img" aria-label="Illustration of two team members" style="left:12px;top:13px;width:34px;height:30px"></div>
    <div class="abs" style="left:56px;top:17px"><div class="name">Pro</div><div class="sub">per year</div></div>
    <div class="price" style="top:20px">$36</div>
    <p class="desc" style="top:58px">For small teams up to 10 members. This plan gives you ultimate tool to manage your team's passwords and collaborate internally. Available on all your devices.</p>
    <div class="btn outline" style="left:9px;top:105px;width:103px;height:29px">Learn more <svg width="10" height="10" viewBox="0 0 10 10" style="color:#0b55c9"><use href="#i-arrow"/></svg></div>
    <div class="btn" style="left:118px;top:105px;width:105px;height:29px">Downgrade <svg width="10" height="10" viewBox="0 0 10 10" style="color:#fff;transform:rotate(90deg)"><use href="#i-arrow"/></svg></div>
  </div>
  <nav class="nav" style="left:9px;top:475px;width:233px;height:61px">
    <div class="nav-item"><span class="ico"><svg width="11" height="11" viewBox="0 0 10 10"><use href="#i-info"/></svg></span>Information</div>
    <div class="nav-item active"><span class="ico"><svg width="11" height="11" viewBox="0 0 10 10" style="color:#0a63e8"><use href="#i-lock"/></svg></span>Access</div>
  </nav>
</section>

</body>
</html>
```